Brennick Framing Company - Card Design

I am looking to use the logo designs that you already did for me to develop a business card. I would like the card to have a black background and be double sided. I want white and green logo and text. I have attached an inspiration photo of a look that I like. I would like to use the Vertical Logo attached to take up the full front side of the card. On the back where I have my name and information, I would like to have the horizontal logo or maybe even just the image of the 'A' and trees without the text. I am open, but I am looking for something clean and simple and I want the green to really pop! Additional files can be found under Design #: 64093528

Target Market(s)

Homeowners

Industry/Entity Type

Construction

Contact Information for Business Card

Name: Marcus Brennick, Title: Project Manager, Phone: 647.382.9105, Email: brennickframingcompany@quillpost.example, address: 418 Larkspur Ln, Felton, CA 95018, Lic# 5836214

Colors
00AB8E
00BBA5
67D7C9
C6EFE9
E9F9F6

Requirements
Nice to have
• I would like to see the logos that I have already got from ArtSwarm, though I am open to new ones

```html
<!DOCTYPE html>
<html lang="en">
<head>
<meta charset="utf-8">
<title>Brennick Framing Company – Business Card</title>
<link rel="stylesheet" href="https://fonts.googleapis.com/css2?family=Poppins:wght@400;600;700&display=swap">
<style>
  :root {
    --backdrop: #d4d5d8;
    --card: #111111;
    --green: #6db54a;
    --white: #ffffff;
  }
  * { margin: 0; padding: 0; box-sizing: border-box; }
  html, body { width: 900px; height: 1200px; overflow: hidden; }
  body {
    background: var(--backdrop);
    font-family: "Poppins", sans-serif;
    position: relative;
  }
  .card {
    position: absolute;
    left: 119px;
    width: 662px;
    height: 375px;
    background: var(--card);
    overflow: hidden;
  }
  .card--front { top: 203px; }
  .card--back { top: 620px; }

  /* Front */
  .front-brand {
    position: absolute;
    left: 0; right: 0; top: 128px;
    text-align: center;
  }
  .brand-row {
    display: flex;
    justify-content: center;
    align-items: center;
    gap: 88px;
    height: 60px;
  }
  .brand-mark {
    width: 30px; height: 30px;
    background: var(--green);
  }
  .estd {
    font-size: 10px;
    letter-spacing: 3px;
    color: var(--white);
    border-top: 1px solid var(--green);
    border-bottom: 1px solid var(--green);
    padding: 1px 2px;
    margin-top: 24px;
  }
  .brand-name {
    font-weight: 600;
    color: var(--white);
    text-transform: uppercase;
  }
  .front-brand .brand-name {
    margin-top: 14px;
    font-size: 36px;
    line-height: 1.05;
    letter-spacing: 1px;
  }
  .front-brand .brand-name small {
    display: block;
    font-size: 17px;
    font-weight: 600;
    letter-spacing: 5px;
    margin-top: 4px;
  }

  /* Back */
  .back-brand {
    position: absolute;
    left: 64px; top: 118px;
    width: 260px;
  }
  .back-brand .brand-mark { width: 26px; height: 26px; margin-bottom: 14px; }
  .back-brand .brand-name { font-size: 28px; line-height: 1.12; }

  .divider {
    position: absolute;
    left: 360px; top: 96px;
    width: 1px; height: 188px;
    background: var(--white);
  }
  .contact {
    position: absolute;
    left: 384px; top: 92px;
    width: 262px;
    color: var(--white);
  }
  .contact-name {
    font-size: 24px;
    font-weight: 700;
    color: var(--green);
    line-height: 1.15;
    letter-spacing: 0.3px;
    white-space: nowrap;
  }
  .contact-title { font-size: 15px; letter-spacing: 0.5px; margin-top: 2px; }
  .rule { width: 150px; height: 1px; background: var(--green); margin: 7px 0 8px; }
  .contact-address { font-size: 14px; line-height: 19px; letter-spacing: 0.8px; }
  .contact-list { list-style: none; }
  .contact-list li {
    display: flex; align-items: center; gap: 6px;
    font-size: 14px; letter-spacing: 0.6px; height: 23px;
    white-space: nowrap;
  }
  .contact-list .phone { letter-spacing: 3px; }
  .contact-list svg { width: 14px; height: 14px; fill: var(--green); flex: none; }
</style>
</head>
<body>

<section class="card card--front" aria-label="Card front">
  <div class="front-brand">
    <div class="brand-row">
      <span class="estd">ESTD</span>
      <div class="brand-mark"></div>
      <span class="estd">2020</span>
    </div>
    <h1 class="brand-name">Brennick<small>Framing Company</small></h1>
  </div>
</section>

<section class="card card--back" aria-label="Card back">
  <div class="back-brand">
    <div class="brand-mark"></div>
    <p class="brand-name">Brennick<br>Framing<br>Company</p>
  </div>
  <div class="divider"></div>
  <div class="contact">
    <h2 class="contact-name">MARCUS BRENNICK</h2>
    <p class="contact-title">Project Manager</p>
    <div class="rule"></div>
    <p class="contact-address">418 Larkspur Ln,<br>Felton CA 95018</p>
    <div class="rule"></div>
    <ul class="contact-list">
      <li class="phone">
        <svg viewBox="0 0 24 24" aria-hidden="true"><path d="M6.6 10.8a15.1 15.1 0 0 0 6.6 6.6l2.2-2.2a1 1 0 0 1 1-.25 11.4 11.4 0 0 0 3.6.57 1 1 0 0 1 1 1V20a1 1 0 0 1-1 1A17 17 0 0 1 3 4a1 1 0 0 1 1-1h3.5a1 1 0 0 1 1 1c0 1.25.2 2.45.57 3.57a1 1 0 0 1-.25 1z"/></svg>
        647-382-9105
      </li>
      <li>
        <svg viewBox="0 0 24 24" aria-hidden="true"><path d="M2 5h20v14H2z"/><path d="M3 6l9 7 9-7" fill="none" stroke="#111" stroke-width="1.6"/></svg>
        info@brennick.example
      </li>
      <li>
        <svg viewBox="0 0 24 24" aria-hidden="true"><circle cx="12" cy="12" r="10"/><path d="M2 12h20M12 2c3 3 3 17 0 20M12 2c-3 3-3 17 0 20M4 7h16M4 17h16" fill="none" stroke="#111" stroke-width="1.3"/></svg>
        www.brennick.example
      </li>
      <li>
        <svg viewBox="0 0 24 24" aria-hidden="true"><path d="M12 2l8 3v6c0 5-3.5 9-8 11-4.5-2-8-6-8-11V5z"/><path d="M8 12l3 3 5-6" fill="none" stroke="#111" stroke-width="2"/></svg>
        Lic# 5836214
      </li>
    </ul>
  </div>
</section>

</body>
</html>
```